Refresh Application User Interface

Pellmark wishes to update the look of its business applications. Two representative forms are shown below. Please note, we are not considering changes in functionality or usability. Our goal is a cleaner, more contemporary design.

Industry/Entity Type

Business

```html
<!DOCTYPE html>
<html lang="en">
<head>
<meta charset="utf-8">
<title>Purchase Order – Pellmark</title>
<link href="https://fonts.googleapis.com/css2?family=Exo+2:wght@400;500;600;700&family=Roboto:wght@400;500;700&display=swap" rel="stylesheet">
<style>
:root{
  --black:#000;
  --blue:#0a55a8;
  --blue-dark:#08478f;
  --blue-bright:#1478e6;
  --green:#82c341;
  --text:#333;
  --muted:#555;
  --field:#f2f2f2;
  --line:#dcdcdc;
  --white:#fff;
}
*{box-sizing:border-box;margin:0;padding:0}
html,body{width:1200px;height:1190px;overflow:hidden;background:var(--white)}
body{position:relative;font-family:"Exo 2",sans-serif;color:var(--text);font-size:12px}
.abs{position:absolute}
.topbar{left:0;top:0;width:1200px;height:46px;background:var(--black);color:var(--white);font-size:12px}
.topbar .who{left:21px;top:14px}
.topbar .hl{color:var(--green);font-weight:600}
.topbar .links{right:18px;top:15px;display:flex;gap:15px;font-family:Roboto,sans-serif}
.modules{left:14px;top:60px;display:flex;font-family:Roboto,sans-serif;font-size:12px}
.modules div{width:109px;height:34px;border:1px solid var(--line);border-left:none;display:flex;align-items:center;justify-content:center;color:var(--text)}
.modules .active{width:95px;background:linear-gradient(90deg,var(--blue-bright),var(--blue));color:var(--white);font-weight:700;border:none}
.brand{left:964px;top:60px;height:34px;display:flex;align-items:center;gap:6px;font-family:"Exo 2",sans-serif;font-weight:700;font-size:31px;color:var(--blue);letter-spacing:1px}
.brand i{width:14px;height:14px;border-radius:50%;background:var(--green);display:block}
.subnav{left:0;top:106px;width:1200px;height:42px;background:var(--green)}
.subnav span{position:absolute;top:14px;color:var(--white);font-weight:500;font-size:12px}
.title{left:13px;top:172px;font-size:15px;font-weight:600;color:#222}
.doctabs{left:878px;top:170px;display:flex;font-family:Roboto,sans-serif;font-size:11.5px}
.doctabs div{position:relative;height:33px;width:79px;display:flex;align-items:center;justify-content:center;border:1px solid var(--line);border-bottom:none;color:var(--text);overflow:hidden}
.doctabs .active{width:76px;background:var(--blue);color:var(--white);font-weight:700;border:none}
.doctabs .done::after{content:"";position:absolute;right:0;top:0;border-top:22px solid var(--green);border-left:28px solid transparent}
.doctabs .done svg{position:absolute;right:2px;top:1px;z-index:1}
.toolbar{left:12px;top:203px;width:1178px;height:35px;background:var(--blue);color:var(--white);font-family:Roboto,sans-serif;font-size:12px}
.tool{position:absolute;top:0;height:35px;background:var(--blue-dark);border-right:2px solid var(--blue);display:flex;align-items:center;justify-content:center;gap:8px}
.action{position:absolute;top:10px;display:flex;align-items:center;gap:6px}
.panel{left:11px;top:252px;width:1179px;height:908px;border:1px solid var(--line)}
.label{position:absolute;color:var(--text);font-size:12px;font-weight:500}
.field{position:absolute;background:var(--field);font-size:12px;font-weight:500;padding-left:15px;display:flex;align-items:center;color:#333}
.select::after{content:"";position:absolute;right:16px;top:50%;margin-top:-2px;border-left:6px solid transparent;border-right:6px solid transparent;border-top:6px solid #aaa}
.status{position:absolute;font-size:14.5px;font-weight:600}
.green{color:var(--green)}
.blue{color:var(--blue)}
.btn{position:absolute;background:var(--green);color:var(--white);font-weight:500;display:flex;align-items:center;justify-content:center;font-size:12px}
.tabs{left:30px;top:641px;display:flex;font-size:12px}
.tabs div{width:109px;height:34px;border:1px solid var(--line);border-left:none;display:flex;align-items:center;justify-content:center;font-weight:500}
.tabs .active{width:95px;background:linear-gradient(90deg,var(--blue-bright),var(--blue));color:var(--white);border:none;font-weight:600}
.tabs .wide{width:123px}
.inner{left:30px;top:684px;width:1150px;height:428px;border:1px solid var(--line)}
.r{text-align:right}
.req{position:absolute;color:var(--blue-bright);font-size:11px}
.hint{left:0;width:944px;top:1125px;text-align:center;font-size:13px;font-weight:500;color:#444}
</style>
</head>
<body>

<header class="abs topbar">
  <div class="abs who">Logged In As <span class="hl">Dana Hollis</span>
    <svg width="14" height="14" viewBox="0 0 14 14" style="vertical-align:-2px;margin-left:6px"><circle cx="7" cy="7" r="5" fill="none" stroke="#82c341" stroke-width="2" stroke-dasharray="3 1.5"/><circle cx="7" cy="7" r="2" fill="#82c341"/></svg>
    <span style="margin-left:40px">Current Role <span class="hl">Administrator</span> <span class="hl" style="font-size:9px;margin-left:4px">▼</span></span>
  </div>
  <div class="abs links"><span>Touch</span><span>|</span><span>New Tab</span><span>|</span><span>Help</span><span>|</span><span>Support</span><span>|</span><span>Log Out</span></div>
</header>

<nav class="abs modules">
  <div class="active">Home</div><div>eSource</div><div>eBuy</div><div>eRequest</div><div>eSell</div><div>eStock</div><div>ePlan</div><div>Preferences</div>
</nav>
<div class="abs brand">PELLMARK<i></i></div>

<nav class="abs subnav">
  <span style="left:29px">Orders</span><span style="left:94px">Receipts</span><span style="left:166px">Shipments</span><span style="left:251px">Invoices</span><span style="left:323px">Pricing</span><span style="left:388px">Tables</span><span style="left:452px">Reports</span><span style="left:522px">Inquiries</span><span style="left:596px">Periodic Tasks</span><span style="left:700px">Workflows</span>
</nav>

<h1 class="abs title">Purchase Order</h1>
<div class="abs doctabs">
  <div class="active">Header</div>
  <div class="done">Lines<svg width="10" height="8" viewBox="0 0 10 8"><path d="M1 4l3 3 5-6" fill="none" stroke="#fff" stroke-width="1.6"/></svg></div>
  <div>Charges</div>
  <div class="done">Notes<svg width="10" height="8" viewBox="0 0 10 8"><path d="M1 4l3 3 5-6" fill="none" stroke="#fff" stroke-width="1.6"/></svg></div>
</div>

<div class="abs toolbar">
  <div class="tool" style="left:0;width:38px"><svg width="14" height="14" viewBox="0 0 14 14"><path d="M9 3L4 9a1.5 1.5 0 002 2l5-6a2.5 2.5 0 00-4-3L3 8" fill="none" stroke="#9ec3ff" stroke-width="1.3"/></svg></div>
  <div class="tool" style="left:38px;width:38px"><svg width="16" height="12" viewBox="0 0 16 12"><ellipse cx="8" cy="6" rx="7" ry="4.5" fill="none" stroke="#f5d742" stroke-width="1.3"/><circle cx="8" cy="6" r="2" fill="#f5d742"/></svg></div>
  <div class="tool" style="left:76px;width:36px"><svg width="16" height="16" viewBox="0 0 16 16" fill="none" stroke="#fff" stroke-width="1.2"><rect x="1" y="6" width="5" height="5"/><rect x="10" y="1" width="5" height="5"/><rect x="10" y="10" width="5" height="5"/><path d="M6 8h4M10 4v8"/></svg></div>
  <div class="tool" style="left:112px;width:37px"><svg width="18" height="14" viewBox="0 0 18 14"><path d="M1 5h16v8H1z" fill="#f5d742"/><path d="M4 5l3-4h4l3 4" fill="none" stroke="#f5d742" stroke-width="1.3"/></svg></div>
  <div class="tool" style="left:149px;width:37px"><svg width="16" height="16" viewBox="0 0 16 16"><circle cx="8" cy="8" r="7" fill="none" stroke="#e58ad8" stroke-width="1.3"/><text x="8" y="12" text-anchor="middle" fill="#e58ad8" font-size="10" font-family="Roboto">?</text></svg></div>
  <div class="tool" style="left:186px;width:41px"><svg width="16" height="16" viewBox="0 0 16 16" fill="none" stroke="#f5a623" stroke-width="1.6"><path d="M2 14L14 2M2 2l12 12"/></svg></div>
  <div class="tool" style="left:227px;width:112px"><svg width="18" height="18" viewBox="0 0 18 18" fill="none" stroke="#fff" stroke-width="1.2"><path d="M3 1h8l4 4v7M3 1v16h8"/><circle cx="14" cy="14" r="3.5"/><path d="M14 12v4M12 14h4"/></svg>New Post</div>
  <div class="action" style="left:816px"><svg width="12" height="12" viewBox="0 0 12 12" fill="none" stroke="#f5d742" stroke-width="1.6"><circle cx="5" cy="5" r="3.5"/><path d="M7.5 7.5L11 11"/></svg>Search</div>
  <div class="action" style="left:896px"><span style="color:#f5d742;font-weight:700">+</span>New</div>
  <div class="action" style="left:957px"><svg width="12" height="12" viewBox="0 0 12 12" fill="none" stroke="#7fc7ff" stroke-width="1.4"><rect x="1" y="1" width="10" height="10"/><path d="M3 6l2 2 4-5"/></svg>Apply</div>
  <div class="action" style="left:1034px"><svg width="14" height="14" viewBox="0 0 14 14" fill="none" stroke="#fff" stroke-width="1.2"><path d="M2 3h10M5 3V1h4v2M3 3l1 10h6l1-10"/></svg>Delete</div>
  <div class="action" style="left:1114px"><svg width="14" height="12" viewBox="0 0 14 12" fill="none" stroke="#fff" stroke-width="1.2"><path d="M5 1L1 5l4 4M1 5h8a4 4 0 010 8"/></svg>Back</div>
</div>

<main class="abs panel"></main>

<span class="label" style="left:38px;top:277px">Order #</span>
<span class="label" style="left:123px;top:277px">100159</span>
<span class="status green" style="left:302px;top:274px">Regular Purchase Order</span>
<span class="status blue" style="left:974px;top:274px">Hold for Completion</span>

<span class="label" style="left:37px;top:321px">Ship From</span>
<div class="field" style="left:122px;top:311px;width:104px;height:31px">1001</div>
<span class="label" style="left:238px;top:318px;font-size:16px">/</span>
<div class="field" style="left:259px;top:311px;width:42px;height:31px">0</div>

<div class="field" style="left:122px;top:354px;width:548px;height:40px">Harbor Medical Co</div>
<svg class="abs" style="left:687px;top:361px" width="25" height="25" viewBox="0 0 25 25" fill="none" stroke="#82c341" stroke-width="1.3"><circle cx="12.5" cy="12.5" r="11"/><ellipse cx="12.5" cy="12.5" rx="5" ry="11"/><path d="M1.5 12.5h22M3.5 6.5h18M3.5 18.5h18"/></svg>

<span class="label" style="left:38px;top:413px">Address</span>
<div class="field" style="left:122px;top:406px;width:548px;height:40px">12 Tidewater Ln</div>
<div class="field" style="left:122px;top:462px;width:548px;height:40px">12 Tidewater Ln</div>
<span class="status blue" style="left:687px;top:471px;font-size:13.5px">DPA Unconfirmed</span>

<span class="label" style="left:54px;top:529px">City</span>
<div class="field" style="left:122px;top:518px;width:244px;height:40px">Northcove</div>
<span class="label" style="left:398px;top:531px">State</span>
<div class="field" style="left:434px;top:518px;width:43px;height:40px">MA</div>
<div class="field" style="left:530px;top:518px;width:43px;height:40px;justify-content:center;padding:0"><svg width="12" height="10" viewBox="0 0 12 10"><path d="M1 5l3.5 3.5L11 1" fill="none" stroke="#82c341" stroke-width="1.6"/></svg></div>
<span class="label" style="left:590px;top:531px">Accept</span>

<span class="label" style="left:56px;top:579px">Zip</span>
<div class="field" style="left:122px;top:569px;width:244px;height:41px">01977 - 4410</div>
<span class="label" style="left:382px;top:582px">Country</span>
<div class="field" style="left:434px;top:569px;width:140px;height:41px">US</div>
<div class="btn" style="left:586px;top:569px;width:115px;height:41px">ADD CONTACT</div>

<nav class="abs tabs">
  <div class="active">Order Info</div><div>Shipping</div><div>Payment</div><div>Accounts</div><div class="wide">Totals / Approval</div>
</nav>

<section class="abs inner"></section>

<span class="label r" style="left:40px;width:100px;top:712px">Receive At</span>
<div class="field select" style="left:166px;top:702px;width:223px;height:37px">ALCH</div>
<span class="req" style="left:392px;top:700px">*</span>

<span class="label r" style="left:40px;width:98px;top:760px">Carrier</span>
<div class="field select" style="left:166px;top:750px;width:223px;height:37px">SwiftFreight</div>
<span class="req" style="left:392px;top:748px">*</span>

<span class="label" style="left:54px;top:811px">Express Service</span>
<div class="field select" style="left:166px;top:802px;width:223px;height:36px"></div>

<span class="label r" style="left:40px;width:91px;top:859px">FOB</span>
<div class="field select" style="left:166px;top:850px;width:223px;height:36px"></div>

<span class="label" style="left:54px;top:907px">Order Ship Rule</span>
<div class="field select" style="left:166px;top:898px;width:223px;height:36px;padding-left:12px">Partials</div>
<span class="req" style="left:396px;top:898px">*</span>

<span class="label" style="left:54px;top:955px">Line Ship Rlue</span>
<div class="field select" style="left:166px;top:946px;width:223px;height:36px;padding-left:12px">Partials</div>
<span class="req" style="left:396px;top:946px">*</span>

<span class="label r" style="left:440px;width:101px;top:712px">Request Date</span>
<div class="field" style="left:564px;top:702px;width:222px;height:37px">01-07-2018</div>
<svg class="abs" style="left:795px;top:708px" width="22" height="22" viewBox="0 0 22 22"><rect x="1" y="3" width="20" height="18" fill="#eee" stroke="#bbb"/><rect x="1" y="3" width="20" height="5" fill="#e0463a"/><rect x="5" y="1" width="2" height="4" fill="#888"/><rect x="15" y="1" width="2" height="4" fill="#888"/><g fill="#999"><rect x="4" y="10" width="3" height="2"/><rect x="9.5" y="10" width="3" height="2"/><rect x="15" y="10" width="3" height="2"/><rect x="4" y="14" width="3" height="2"/><rect x="9.5" y="14" width="3" height="2"/><rect x="15" y="14" width="3" height="2"/><rect x="4" y="17.5" width="3" height="2"/><rect x="9.5" y="17.5" width="3" height="2"/></g></svg>

<span class="label r" style="left:440px;width:102px;top:760px">Freight Terms</span>
<div class="field select" style="left:564px;top:750px;width:222px;height:37px">Collect</div>

<span class="label r" style="left:440px;width:98px;top:811px">Freight Calc</span>
<div class="field select" style="left:564px;top:802px;width:222px;height:36px"></div>

<span class="label" style="left:867px;top:712px">Customer Ship To</span>
<div class="field" style="left:969px;top:702px;width:135px;height:37px"></div>
<span class="label" style="left:1109px;top:710px;font-size:15px">/</span>
<div class="field" style="left:1123px;top:702px;width:39px;height:37px"></div>

<p class="abs hint">Enter Property Values, and Click Apply</p>

</body>
</html>
```